Halvern Properties Business Cards

I would like a business card that includes myself and my partner.
Includes: Logo, office #, email, website, our names, our numbers and possibly the address. I would also like the logo to be embossed and the card to be horizontal.
There is a photo of our yard signs to give you an idea of the colors of our business.

Target Market(s)

Everyone in real estate market.
We are in a rural area. Our clientele are from all socioeconomic backgrounds.

Industry/Entity Type

Real Estate Agent

Contact Information for Business Card

Company Name: Halvern Properties
Our Names, Titles & Cell #'s : Marla Halvern-Broker (555).316.4827, Tessa Halvern-Realtor (555).627.9154
Office #: (555).841.2600
Website: halvernproperties-example.com
Joint Email: halvern@halvernproperties-example.com
Office Address: 518B W. Cottonwell Ave.
Brenmoor, TX. 70999

Font styles to use
Serif

Requirements
Must have
• HORIZONTAL, Logo, Myself and my partners names, Our cell #'s, our office #, our website, our email address
Nice to have
• Embossed logo, office address, our titles.

```html
<!DOCTYPE html>
<html lang="en">
<head>
<meta charset="utf-8">
<title>Halvern Properties Business Card</title>
<link href="https://fonts.googleapis.com/css2?family=Rokkitt:wght@400;500&display=swap" rel="stylesheet">
<style>
  :root {
    --backdrop: #9b9b9b;
    --card: #fbfbfa;
    --purple: #4a1f60;
    --band: #6e6a9e;
    --band-dark: #5f5b90;
    --muted: #8a8a8a;
    --ink: #2a2a2a;
    --on-band: #f4f3fa;
  }
  * { margin: 0; padding: 0; box-sizing: border-box; }
  html, body { width: 1200px; height: 800px; overflow: hidden; }
  body {
    background: var(--backdrop);
    font-family: "Rokkitt", Georgia, serif;
    position: relative;
  }
  .card {
    position: absolute;
    left: 100px; top: 114px;
    width: 1000px; height: 572px;
    background: var(--card);
    border-radius: 48px;
    overflow: hidden;
  }
  .brand {
    position: absolute; left: 70px; top: 120px;
    display: flex; align-items: center; gap: 18px;
  }
  .brand-dot {
    width: 64px; height: 64px; border-radius: 50%;
    background: var(--purple);
  }
  .brand-name {
    font-weight: 500; font-size: 50px; color: var(--purple); line-height: 1;
  }
  .office {
    position: absolute; right: 80px; top: 52px;
    text-align: right; font-size: 28px; color: var(--ink); line-height: 1.2;
  }
  .icon {
    display: inline-block; vertical-align: middle;
    width: 26px; height: 26px;
  }
  .office .icon { margin-left: 8px; }
  .divider {
    position: absolute; left: 70px; right: 70px; top: 232px;
    height: 2px; background: var(--purple);
  }
  .agent { position: absolute; }
  .agent-name { font-size: 42px; color: var(--purple); line-height: 1; }
  .agent-title { font-size: 21px; color: var(--muted); line-height: 1.2; }
  .agent-phone { font-size: 27px; color: var(--ink); line-height: 1.2; }
  .agent--broker { right: 80px; top: 268px; text-align: right; }
  .agent--broker .icon { margin-left: 8px; }
  .agent--realtor { left: 110px; top: 336px; }
  .agent--realtor .agent-title { padding-left: 14px; }
  .agent--realtor .icon { margin-right: 10px; }
  .contact-band {
    position: absolute; left: 0; right: 0; bottom: 0; height: 124px;
    background: linear-gradient(180deg, var(--band), var(--band-dark));
    display: flex; align-items: center; justify-content: space-between;
    padding: 0 70px 0 90px;
    color: var(--on-band); font-size: 25px;
  }
  .contact-band .icon { margin-right: 10px; }
</style>
</head>
<body>
  <div class="card">
    <div class="brand">
      <div class="brand-dot"></div>
      <div class="brand-name">Halvern Properties</div>
    </div>

    <div class="office">
      <div>518B W. Cottonwell Ave.</div>
      <div>Brenmoor, TX. 70999</div>
      <div>(555).841.2600<svg class="icon" viewBox="0 0 26 26" aria-hidden="true"><circle cx="13" cy="13" r="13" fill="#4a1f60"/><path d="M9 7c1 0 2 2.5 2 3s-1 1-1 1.5 2 3.5 3.5 4c.5 0 1-1 1.5-1s3 1 3 2-1.5 2-2.5 2C11 18 8 13 8 9c0-1 .5-2 1-2z" fill="#fff"/></svg></div>
    </div>

    <div class="divider"></div>

    <div class="agent agent--broker">
      <div class="agent-name">Marla HALVERN</div>
      <div class="agent-title">Broker</div>
      <div class="agent-phone">(555).316.4827<svg class="icon" viewBox="0 0 26 26" aria-hidden="true"><circle cx="13" cy="13" r="13" fill="#4a1f60"/><rect x="9" y="6" width="8" height="14" rx="1.5" fill="none" stroke="#fff" stroke-width="1.6"/><circle cx="13" cy="17.5" r="0.9" fill="#fff"/></svg></div>
    </div>

    <div class="agent agent--realtor">
      <div class="agent-name">Tessa HALVERN</div>
      <div class="agent-title">Realtor</div>
      <div class="agent-phone"><svg class="icon" viewBox="0 0 26 26" aria-hidden="true"><circle cx="13" cy="13" r="13" fill="#4a1f60"/><rect x="9" y="6" width="8" height="14" rx="1.5" fill="none" stroke="#fff" stroke-width="1.6"/><circle cx="13" cy="17.5" r="0.9" fill="#fff"/></svg>(555).627.9154</div>
    </div>

    <div class="contact-band">
      <div class="contact-web"><svg class="icon" viewBox="0 0 26 26" aria-hidden="true"><circle cx="13" cy="13" r="12" fill="#f4f3fa"/><circle cx="13" cy="13" r="8" fill="none" stroke="#6e6a9e" stroke-width="1.5"/><ellipse cx="13" cy="13" rx="3.5" ry="8" fill="none" stroke="#6e6a9e" stroke-width="1.5"/><line x1="5" y1="13" x2="21" y2="13" stroke="#6e6a9e" stroke-width="1.5"/></svg>www.halvernproperties-example.com</div>
      <div class="contact-email"><svg class="icon" viewBox="0 0 26 26" aria-hidden="true"><circle cx="13" cy="13" r="12" fill="#f4f3fa"/><rect x="6.5" y="8.5" width="13" height="9" fill="none" stroke="#6e6a9e" stroke-width="1.5"/><path d="M6.5 8.5l6.5 5 6.5-5" fill="none" stroke="#6e6a9e" stroke-width="1.5"/></svg>halvern@halvernproperties-example.com</div>
    </div>
  </div>
</body>
</html>
```